Great Opportunity !! Masters in Business Analytics College Course

the size is Full Page, with bleed*
8”x 10.75" plus 0.25" bleed.
please leave one inch for footer
the purpose is attract students to join this college program .
this is for students in USA .
college age of around 24 years old
I am looking for a flyer that is unique and shows creativity .
A flyer that people would want to look at it because it is unique.
you can choose either vector, text ,or picture.
if you do picture it should be a white USA citizen wearing a white solid shirt and not long hair

Target Market(s)

USA students about 23 in age to join this college program

Industry/Entity Type

education

Colors
0054AA
0677BA
7BADD7
CADEEF
E8F1F8
0094D4
00A9DD
6FCCEA
C7EBF8
E9F6FB

Requirements
Must have
• the text should not be crowded .. .. .. the ad should not be full of text
Should not have
• not have very large text .. it should not be a flyer that is full of text .. you have to figure out how to avoid looking at the ad and it is very busy with text

```html
<!DOCTYPE html>
<html lang="en">
<head>
<meta charset="UTF-8">
<title>Master's in Business Analytics – Open House Flyer</title>
<link rel="stylesheet" href="https://fonts.googleapis.com/css2?family=Montserrat:wght@400;500;600;700;800&display=swap">
<style>
  :root {
    --page-bg: #e4e4e4;
    --navy: #1c5f9b;
    --gold: #ffd000;
    --tick: #f5c400;
    --pink: #ea1b8a;
    --orange: #f6882c;
    --house-yellow: #e6c200;
    --house-green: #94cb46;
    --white: #ffffff;
    --ink: #1a1a1a;
    --photo-light: #f1f1f1;
    --photo-mid: #d6d6d6;
  }
  * { margin: 0; padding: 0; box-sizing: border-box; }
  html, body { width: 1200px; height: 1200px; overflow: hidden; }
  body {
    background: var(--page-bg);
    font-family: "Montserrat", sans-serif;
    position: relative;
  }
  .flyer {
    position: absolute;
    left: 153px; top: 0;
    width: 893px; height: 1200px;
    background: var(--white);
    overflow: hidden;
  }
  .hero-backdrop {
    position: absolute; left: 0; top: 0; width: 893px; height: 450px;
    background: linear-gradient(90deg, var(--photo-light) 0%, var(--photo-mid) 55%, #e9e9e9 100%);
  }
  .hero-student {
    position: absolute; left: 30px; top: 43px; width: 288px; height: 407px;
    background: linear-gradient(180deg, #d9c3a6 0%, #ece8e4 45%, #f4f4f4 100%);
    border-radius: 120px 120px 0 0;
  }
  .headline {
    position: absolute; left: 392px; top: 38px;
    color: var(--navy); font-weight: 800; font-size: 45px; line-height: 61px;
  }
  .program-name {
    position: absolute; left: 391px; top: 357px;
    color: var(--navy); font-weight: 700; font-size: 25px; line-height: 36px;
  }
  .info-panel { position: absolute; left: 0; top: 446px; }
  .pitch {
    position: absolute; left: 44px; top: 490px;
    color: var(--white); font-weight: 800; font-size: 34px; line-height: 46px;
  }
  .salary {
    position: absolute; left: 42px; top: 584px;
    color: var(--gold); font-weight: 800; font-size: 62px; letter-spacing: -2px;
  }
  .salary-source {
    position: absolute; left: 280px; top: 604px;
    color: var(--white); font-size: 14px; font-weight: 500;
  }
  .tick { width: 1em; height: 1em; flex: none; }
  .roles {
    position: absolute; top: 662px; left: 48px; width: 820px;
    display: flex; gap: 20px; color: var(--white); font-weight: 700; font-size: 21px;
  }
  .roles li, .employers li { list-style: none; display: flex; align-items: center; gap: 9px; white-space: nowrap; }
  .hired-label {
    position: absolute; left: 0; top: 724px; width: 280px; height: 103px;
    background: linear-gradient(90deg, var(--pink), var(--orange));
    border-radius: 0 22px 22px 0;
    color: var(--white); font-weight: 700; font-size: 26px; line-height: 39px;
    padding: 12px 0 0 44px;
  }
  .employers {
    position: absolute; left: 310px; top: 735px;
    display: grid; grid-template-columns: 188px 154px auto; row-gap: 8px;
    color: var(--white); font-weight: 700; font-size: 27px;
  }
  .employers .tick { width: 26px; height: 26px; }
  .accreditation {
    position: absolute; left: 30px; width: 833px; top: 855px;
    text-align: center; color: var(--white); font-weight: 800; font-size: 26px; line-height: 37px;
  }
  .open-house {
    position: absolute; left: 159px; top: 945px; width: 575px; height: 74px;
    display: flex; border-radius: 12px; overflow: hidden;
  }
  .open-house-tag {
    width: 223px; background: var(--house-yellow);
    display: flex; align-items: center; justify-content: center;
    color: var(--white); font-weight: 800; font-size: 25px;
  }
  .open-house-details {
    flex: 1; background: var(--house-green); color: var(--white);
    padding: 12px 0 0 17px;
  }
  .open-house-date { font-weight: 700; font-size: 19px; white-space: nowrap; }
  .open-house-contact {
    display: flex; align-items: center; gap: 8px;
    font-size: 15px; margin-top: 6px; white-space: nowrap;
  }
  .open-house-contact strong { font-weight: 700; }
  .facts {
    position: absolute; left: 47px; top: 1043px; width: 810px;
    display: flex; align-items: center; gap: 14px;
    color: var(--white); font-weight: 700; font-size: 15.5px; white-space: nowrap;
  }
  .facts .divider { width: 2px; height: 20px; background: var(--gold); }
  .footer-location {
    position: absolute; left: 44px; top: 1120px;
    color: var(--ink); font-size: 16px; font-weight: 500;
  }
</style>
</head>
<body>
<svg width="0" height="0" style="position:absolute">
  <defs>
    <symbol id="tick" viewBox="0 0 24 24">
      <circle cx="12" cy="12" r="12" fill="#f5c400"/>
      <path d="M6.5 12.5l3.6 3.5 7.4-7.6" fill="none" stroke="#fff" stroke-width="2.8" stroke-linecap="round" stroke-linejoin="round"/>
    </symbol>
    <linearGradient id="panelGradient" x1="0" y1="0" x2="0.2" y2="1">
      <stop offset="0" stop-color="#0aa8da"/>
      <stop offset="0.45" stop-color="#0a95cf"/>
      <stop offset="1" stop-color="#176ea7"/>
    </linearGradient>
  </defs>
</svg>

<main class="flyer">
  <div class="hero-backdrop" role="img" aria-label="Blurred campus building in soft grey tones"></div>
  <div class="hero-student" role="img" aria-label="Smiling student in a white top holding books"></div>

  <h1 class="headline">Do you have an<br>ANALYTICAL mind<br>and seeking a<br>PROFITABLE<br>career?</h1>
  <p class="program-name">A Master's in Business Analytics-<br>Ridgecrest State University **</p>

  <svg class="info-panel" width="893" height="642" viewBox="0 0 893 642">
    <path d="M0 0 H600 Q636 0 636 36 V60 Q636 82 660 70 L780 2 Q784 0 790 0 H893 V642 H0 Z" fill="url(#panelGradient)"/>
  </svg>

  <p class="pitch">can prepare you for in-demand<br>jobs with a median salary of</p>
  <p class="salary">$100k+</p>
  <p class="salary-source">(National Workforce Data Survey 2023)</p>

  <ul class="roles">
    <li><svg class="tick"><use href="#tick"/></svg>BI Developer</li>
    <li><svg class="tick"><use href="#tick"/></svg>Data Analyst</li>
    <li><svg class="tick"><use href="#tick"/></svg>Data Scientist</li>
    <li><svg class="tick"><use href="#tick"/></svg>Data Developer</li>
  </ul>

  <p class="hired-label">Graduates<br>were hired at:</p>
  <ul class="employers">
    <li><svg class="tick"><use href="#tick"/></svg>Hallvane</li>
    <li><svg class="tick"><use href="#tick"/></svg>Corvex</li>
    <li><svg class="tick"><use href="#tick"/></svg>Stonebridge</li>
    <li><svg class="tick"><use href="#tick"/></svg>Brennick</li>
    <li><svg class="tick"><use href="#tick"/></svg>Voltera</li>
  </ul>

  <p class="accreditation">*** GBSA Accreditation. A distinction held by only 5%<br>of business schools globally.</p>

  <section class="open-house">
    <div class="open-house-tag">OPEN HOUSE</div>
    <div class="open-house-details">
      <p class="open-house-date">Wednesday, April 20, 7:30 pm.</p>
      <p class="open-house-contact">
        <svg width="20" height="14" viewBox="0 0 20 14"><rect width="20" height="14" rx="2" fill="#fff"/><path d="M1 1.5l9 6.5 9-6.5" fill="none" stroke="#94cb46" stroke-width="2"/></svg>
        <span><strong>info@ridgecrest.edu</strong> for the link!</span>
      </p>
    </div>
  </section>

  <p class="facts">
    <span>Men &amp; Women Program</span><span class="divider"></span>
    <span>21 months</span><span class="divider"></span>
    <span>Hybrid with one weekly in-person evening meeting</span>
  </p>

  <p class="footer-location">Brookfield, NJ, USA</p>
</main>
</body>
</html>
```